cartNest - a stylish trolley for apartments

We neede a simple website to sell our Trolley, for apartment use.
The colour theme is red, blask & white. Our logo is attached and this needs to be on the Home page.
The website only needs a Home Page plus 4 other pges.
In the attachment you will find a site map.

You can check out the following two sites to see what I like:
www.plinvex.example/design-showcase-inspiration/minimalist-portfolio-website/
www.brostaquill.example/inspiration/40-beautiful-web-design-portfolios/ in this site especially
Dario Pesqueta
Q L Smithy
Nine 86 Studio
Albert Crisp

And especially Lamp - I ike the simpicity of the site esp as we are only selling one product

Target Market(s)

Apartment dwellers

Industry/Entity Type

Apartment

Requirements
Must have
• This website must have 4 pages.
We need Zanto, Fundline and Quibpay portals.
Order Form for Trolley
Payment form.

```html
<!DOCTYPE html>
<html lang="en">
<head>
<meta charset="utf-8">
<title>cartNest - Home</title>
<link rel="stylesheet" href="https://fonts.googleapis.com/css2?family=Arimo:wght@400;700&family=Tinos&display=swap">
<style>
:root{
  --black:#0b0b0b;
  --bar:#161616;
  --white:#ffffff;
  --red:#c8102e;
  --gold:#f6c75a;
  --yellow:#f3c623;
  --grey-text:#5a5a5a;
  --grey-light:#efefef;
  --border:#b9b9b9;
}
*{box-sizing:border-box;margin:0;padding:0}
html,body{width:1200px;height:1113px;overflow:hidden;background:var(--white);font-family:"Arimo",Arial,sans-serif}
.page{position:relative;width:1200px;height:1113px}
.abs{position:absolute}
.topbar{left:0;top:0;width:1200px;height:47px;background:linear-gradient(#222,#0c0c0c);box-shadow:0 2px 4px rgba(0,0,0,.4)}
.nav a{position:absolute;color:var(--white);font-weight:700;font-size:18px;text-decoration:none;white-space:nowrap}
.brand-badge{left:122px;top:-20px;width:216px;height:216px;border-radius:50%;background:radial-gradient(circle at 50% 40%,#2a2a2a,#000 70%);box-shadow:0 2px 6px rgba(0,0,0,.5)}
.brand-name{left:180px;top:64px;color:var(--white);font-weight:700;font-size:24px}
.cart-links{left:902px;top:68px;font-size:13px;font-weight:700;color:var(--grey-text)}
.slider{left:0;top:0}
.caption{left:126px;top:426px;width:500px;height:62px;background:linear-gradient(90deg,rgba(0,0,0,.75),rgba(0,0,0,.35))}
.caption h2{position:absolute;left:22px;top:5px;color:var(--gold);font-size:25px;font-weight:700}
.caption p{position:absolute;left:22px;top:36px;color:var(--white);font-size:16px;font-weight:700;white-space:nowrap}
.pager{left:880px;top:463px;width:186px;height:25px;background:#1c1c1c;border-radius:14px 0 0 0;color:var(--white);font-family:"Tinos",serif;font-size:18px;padding-left:54px;line-height:27px;word-spacing:6px}
.pager .on{color:var(--gold);font-weight:700}
.box{top:561px;width:312px;height:181px;border:1px solid var(--border);border-radius:4px;background:linear-gradient(#fff 40%,#ececec);overflow:hidden}
.box-head{height:33px;background:linear-gradient(#3a3a3a,#000 60%);border-bottom:3px solid var(--yellow);color:var(--white);font-size:21px;font-weight:700;padding:3px 0 0 20px}
.entry{position:absolute;left:12px;width:295px}
.entry .thumb{position:absolute;left:0;top:0;width:46px;height:48px;border:1px solid #999;background:linear-gradient(#d9c9b9,#8b6f5c)}
.entry p{position:absolute;left:52px;top:0;font-size:11px;font-weight:700;color:var(--grey-text);line-height:13px;width:245px}
.entry .more{position:absolute;right:0;top:35px;font-size:9px;font-weight:700;color:#222}
.view-more{position:absolute;left:15px;top:166px;font-size:9px;font-weight:700;color:#222}
.info{position:absolute;left:15px;font-size:15px;font-weight:700;color:var(--grey-text)}
.info b{color:#111}
.pay{position:absolute;top:131px;font-size:13px;font-weight:700;color:#333}
.about-band{left:0;top:792px;width:1200px;height:241px;background:var(--grey-light)}
.about-title{left:117px;top:813px;font-family:"Tinos",serif;font-size:19px;color:var(--grey-text)}
.about-title b{font-family:"Arimo",sans-serif;color:#111}
.about-text{left:117px;top:846px;width:460px;font-size:13px;font-weight:700;color:var(--grey-text);line-height:20px}
.btn{left:117px;top:918px;width:70px;height:31px;border:1px solid #999;border-radius:3px;background:linear-gradient(#fff,#e4e4e4);font-size:12px;color:#333;text-align:center;line-height:30px}
.gallery-title{left:647px;top:813px;font-size:19px;font-weight:700;color:var(--grey-text)}
.thumbimg{top:842px;width:104px;height:100px;border:3px solid #c9c9c9}
.footer{left:0;top:1033px;width:1200px;height:80px;background:linear-gradient(#262626,#080808);border-top:3px solid #cfcfcf}
.copy{left:116px;top:1067px;color:var(--white);font-size:13px;font-weight:700}
.foot-nav a{font-size:16px}
</style>
</head>
<body>
<div class="page">

  <header>
    <div class="abs topbar"></div>
    <div class="abs brand-badge"></div>
    <div class="abs brand-name">cartNest</div>
    <nav class="nav">
      <a style="left:437px;top:13px">cartNest</a>
      <a style="left:582px;top:13px">Gallery</a>
      <a style="left:694px;top:13px">Contact us</a>
      <a style="left:847px;top:13px">Shopping cart payment</a>
    </nav>
    <div class="abs cart-links">My cart &nbsp;|&nbsp; Chek out</div>
    <svg class="abs" style="left:1034px;top:66px" width="40" height="32" viewBox="0 0 40 32" aria-hidden="true">
      <path d="M1 3h7l5 18h21l4-13H11" fill="none" stroke="#999" stroke-width="2"/>
      <circle cx="15" cy="27" r="3" fill="#999"/><circle cx="31" cy="27" r="3" fill="#999"/>
    </svg>
  </header>

  <section class="hero">
    <svg class="abs slider" width="1200" height="520" viewBox="0 0 1200 520">
      <defs>
        <linearGradient id="heroTone" x1="0" y1="0" x2="1" y2="1">
          <stop offset="0" stop-color="#2c2c38"/>
          <stop offset=".45" stop-color="#c9bfb3"/>
          <stop offset=".75" stop-color="#9a8a78"/>
          <stop offset="1" stop-color="#6b4a33"/>
        </linearGradient>
        <filter id="soft" x="-5%" y="-5%" width="110%" height="115%"><feDropShadow dx="0" dy="3" stdDeviation="4" flood-opacity=".35"/></filter>
      </defs>
      <path d="M116 135 Q597 20 1078 135 V497 H116 Z" fill="#fff" filter="url(#soft)"/>
      <path role="img" aria-label="Chrome birdcage luggage trolley holding red suitcases in an apartment hallway" d="M126 145 Q597 40 1064 145 V488 H126 Z" fill="url(#heroTone)"/>
      <path d="M116 298 a18 18 0 0 1 0 36 Z" fill="#fff"/>
      <path d="M122 316 l9 -8 v16 Z" fill="#111"/>
      <path d="M1078 298 a18 18 0 0 0 0 36 Z" fill="#fff"/>
      <path d="M1071 316 l-9 -8 v16 Z" fill="#111"/>
    </svg>
    <div class="abs caption">
      <h2>Lorem ipsum dolor</h2>
      <p>Lorem ipsum dolor sit amet, consectetur adipiscing elit.</p>
    </div>
    <div class="abs pager">1 2 <span class="on">3</span> 4 5</div>
  </section>

  <section class="features">
    <article class="abs box" style="left:116px">
      <div class="box-head">cartNest</div>
      <div class="entry" style="top:46px">
        <div class="thumb" role="img" aria-label="Customer portrait"></div>
        <p>IT LOOKS GREAT!&nbsp; Designed along the lines of the familiar hotel “birdcage” luggage trolley,</p>
        <span class="more">&gt;&gt; Read More</span>
      </div>
      <div class="entry" style="top:106px">
        <div class="thumb" role="img" aria-label="Customer portrait" style="background:linear-gradient(#eee,#9aa)"></div>
        <p>IT LOOKS GREAT!&nbsp; Designed along the lines of the familiar hotel “birdcage” luggage trolley,</p>
        <span class="more" style="top:37px">&gt;&gt; Read More</span>
      </div>
      <span class="view-more">▾ View More</span>
    </article>

    <article class="abs box" style="left:441px">
      <div class="box-head">Contact us</div>
      <p class="info" style="top:52px">Phone : 5550 1234 678</p>
      <p class="info" style="top:88px">Email : <b>hello@cartnest.example</b></p>
      <p class="info" style="top:130px;left:13px">cartNest Contact detail:</p>
    </article>

    <article class="abs box" style="left:766px">
      <div class="box-head">Shopping cart payment</div>
      <p class="info" style="top:52px;left:20px">Order form ▾</p>
      <p class="info" style="top:88px;left:19px">Payment from Incl</p>
      <span class="pay" style="left:20px">Zanto</span>
      <span class="pay" style="left:66px">Fundline</span>
      <span class="pay" style="left:130px">Quibpay</span>
    </article>
  </section>

  <section class="about">
    <div class="abs about-band"></div>
    <h3 class="abs about-title">About <b>cartNest :</b></h3>
    <p class="abs about-text">cartNest originated from our personal experience of apartment living, and the hassle of taking shopping, luggage, etc, from your car to your apartment. We have sourced trolleys from all over the place,</p>
    <div class="abs btn">Read More</div>

    <h3 class="abs gallery-title">Gallery</h3>
    <div class="abs thumbimg" style="left:648px;background:linear-gradient(#8a4a3a,#d8cfc4)" role="img" aria-label="Trolley wheel close-up with red case"></div>
    <div class="abs thumbimg" style="left:757px;background:linear-gradient(#9a9a9a,#5a4a40)" role="img" aria-label="Trolley loaded with luggage in a lift"></div>
    <div class="abs thumbimg" style="left:866px;background:linear-gradient(#7a7570,#4a4440)" role="img" aria-label="Trolley being loaded beside a car in a garage"></div>
    <div class="abs thumbimg" style="left:975px;background:linear-gradient(#dfe6ea,#9fb0b8)" role="img" aria-label="Empty chrome trolley frame"></div>
    <svg class="abs" style="left:647px;top:951px" width="432" height="30" viewBox="0 0 432 30" aria-hidden="true">
      <circle cx="14" cy="15" r="13" fill="#f4f4f4" stroke="#888" stroke-width="1.5"/>
      <path d="M9 15 l8 -6 v12 Z" fill="#333"/>
      <circle cx="417" cy="15" r="13" fill="#f4f4f4" stroke="#888" stroke-width="1.5"/>
      <path d="M422 15 l-8 -6 v12 Z" fill="#333"/>
    </svg>
  </section>

  <footer>
    <div class="abs footer"></div>
    <p class="abs copy">© 2012 All Rights Reserved cartNest</p>
    <nav class="nav foot-nav">
      <a style="left:537px;top:1065px">cartNest</a>
      <a style="left:656px;top:1065px">Gallery</a>
      <a style="left:749px;top:1065px">Contact us</a>
      <a style="left:876px;top:1065px">Shopping cart payment</a>
    </nav>
  </footer>

</div>
</body>
</html>
```